Hi,

I have just started up a business called VOLMIRA in Melbourne. We run fun street art tours around Melbourne's CBD.

I need to create a design for the back side of my business cards. I have designed the front side (simply with my logo) however, I am having trouble designing the reverse side in a professional manner. I have attached pictures of what I have done.

The picture attached titled "VOLMIRA Business Cards Back" has all the information that I require on the back side of my business cards; although displayed in an amateur and simple way. As displayed in the picture, I need: the VOLMIRA logo, the website URL, the booking details (phone - 0468 152 837 & email - bookings@volmira-example.com.au) and the service description ($20, One Hour, Tours Daily, Meet at Halberton St Station). I would also like to use the font in the picture supplied which is "source-sans-pro".

The VOLMIRA tours are for tourists and are relaxed, entertaining and fun! I would like the design to reflect this.

Target Market(s)

Backpackers & University Students

Industry/Entity Type

Business

Requirements
Must have
• The VOLMIRA logo, the website URL, the booking details (phone - 0468 152 837 & email - bookings@volmira-example.com.au) and the service description ($20, One Hour, Tours Daily, Meet at Halberton St Station).

```html
<!DOCTYPE html>
<html lang="en">
<head>
<meta charset="utf-8">
<title>Volmira Art Tours – Card Back</title>
<link rel="stylesheet" href="https://fonts.googleapis.com/css2?family=Aladin&family=Cinzel:wght@400&family=Crimson+Text:ital@1&display=swap">
<style>
  :root {
    --salmon: #f28488;
    --blush: #f7c3c5;
    --overlay-pink: rgba(244, 120, 128, 0.55);
    --overlay-blush: rgba(248, 190, 192, 0.6);
    --mauve-veil: rgba(110, 70, 85, 0.45);
    --ink: #111111;
    --umbrella-ink: #2a1820;
  }
  html, body {
    margin: 0;
    padding: 0;
    width: 1200px;
    height: 693px;
    overflow: hidden;
    background: #ffffff;
  }
  .card {
    position: relative;
    width: 1200px;
    height: 693px;
    overflow: hidden;
    background: var(--blush);
  }
  .card > * { position: absolute; }
  .photo-umbrellas {
    left: 271px; top: 0; width: 929px; height: 693px;
    background:
      radial-gradient(ellipse 300px 220px at 600px 200px, rgba(230, 60, 70, 0.9), transparent 70%),
      radial-gradient(ellipse 260px 180px at 420px 560px, rgba(170, 60, 200, 0.8), transparent 70%),
      radial-gradient(ellipse 260px 200px at 250px 200px, rgba(60, 150, 230, 0.8), transparent 70%),
      radial-gradient(ellipse 240px 200px at 700px 420px, rgba(70, 190, 230, 0.75), transparent 70%),
      radial-gradient(ellipse 220px 180px at 300px 380px, rgba(120, 220, 90, 0.7), transparent 70%),
      linear-gradient(160deg, #b9c4a4 0%, #7fb7c9 45%, #4f6f72 100%);
  }
  .band-top {
    left: 0; top: 0; width: 271px; height: 277px;
    background: var(--salmon);
  }
  .band-lower {
    left: 0; top: 277px; width: 271px; height: 416px;
    background: var(--blush);
    border-top-left-radius: 14px;
  }
  .veil-top {
    left: 271px; top: 0; width: 274px; height: 277px;
    background: var(--overlay-pink);
  }
  .veil-lower {
    left: 271px; top: 277px; width: 274px; height: 416px;
    background: var(--overlay-blush);
  }
  .veil-column {
    left: 229px; top: 133px; width: 223px; height: 560px;
    background: var(--mauve-veil);
    border-top-left-radius: 10px;
    border-top-right-radius: 10px;
  }
  .brand-name {
    left: 820px; top: 180px; margin: 0;
    font-family: "Cinzel", serif;
    font-size: 40px;
    letter-spacing: 2px;
    color: var(--umbrella-ink);
  }
  .title {
    left: 58px; top: 26px; margin: 0;
    font-family: "Aladin", cursive;
    font-weight: 400;
    font-size: 82px;
    line-height: 1.1;
    letter-spacing: 6px;
    word-spacing: 34px;
    color: var(--ink);
  }
  .guide-name, .guide-phone, .offer {
    font-family: "Cinzel", serif;
    color: var(--ink);
    margin: 0;
    line-height: 1;
  }
  .guide-name { left: 34px; top: 196px; font-size: 44px; }
  .guide-phone { left: 32px; top: 244px; font-size: 48px; }
  .offer { font-size: 40px; }
  .offer-price { left: 176px; top: 346px; }
  .offer-days { left: 176px; top: 390px; }
  .offer-meet { left: 176px; top: 440px; font-size: 24px; }
  .contact {
    left: 40px; width: 462px; margin: 0;
    text-align: center;
    font-family: "Crimson Text", serif;
    font-style: italic;
    font-size: 33px;
    line-height: 1.2;
    color: var(--ink);
  }
  .contact-web { top: 516px; }
  .contact-mail { top: 566px; }
</style>
</head>
<body>
  <main class="card">
    <div class="photo-umbrellas" role="img" aria-label="Photo of colourful umbrellas hanging in a shopping arcade with a smiling tour guide holding a rainbow umbrella"></div>
    <div class="veil-top"></div>
    <div class="veil-lower"></div>
    <div class="band-top"></div>
    <div class="band-lower"></div>
    <div class="veil-column"></div>

    <p class="brand-name">VOLMIRA</p>
    <h1 class="title">Art Tours</h1>
    <p class="guide-name">Jules</p>
    <p class="guide-phone">0468152837</p>
    <p class="offer offer-price">$20 1 Hour Tour</p>
    <p class="offer offer-days">Tours : Daily</p>
    <p class="offer offer-meet">Meet at Halberton St Station</p>
    <p class="contact contact-web">www.volmira-example.com.au</p>
    <p class="contact contact-mail">bookings@volmira-example.com.au</p>
  </main>
</body>
</html>
```